marcello's mobile mechanic

a business card that will get attention from clients
- name of the business: TREVISKE ROADSIDE REPAIR
- we currently do not have a logo and do not need one at the moment, happy for the designers to just put the business name on the card using appropriate fonts

Target Market(s)

low cost mobile repairs

Industry/Entity Type

Business

Contact Information for Business Card

attracts customers

Font styles to use
Sans Serif

Colors
0255a3
fbee3d
000000

Requirements
Must have
• (555) 381-7094
• Marcello Treviske
• for lower income target market
Nice to have
• "we save you money"
• Easy to read
Should not have
• nothing comes to mind

```html
<!DOCTYPE html>
<html lang="en">
<head>
<meta charset="utf-8">
<title>Treviske Roadside Repair – Business Card</title>
<link href="https://fonts.googleapis.com/css2?family=Cinzel:wght@400;600&family=Cormorant+Garamond:wght@500&display=swap" rel="stylesheet">
<style>
  :root {
    --backdrop: #2c2522;
    --card-black: #0b0b0b;
    --card-black-top: #3a3a3a;
    --brand-yellow: #fbee3d;
    --ink-black: #000000;
    --phone-grey: #d6d6d6;
    --rule-dark: #1a1a1a;
  }
  * { margin: 0; padding: 0; box-sizing: border-box; }
  html, body {
    width: 1200px;
    height: 844px;
    overflow: hidden;
    background: var(--backdrop);
  }
  .stage {
    position: relative;
    width: 1200px;
    height: 844px;
    display: flex;
    align-items: center;
    justify-content: center;
    gap: 60px;
  }
  .card {
    position: relative;
    width: 500px;
    height: 286px;
    border-radius: 3px;
    box-shadow: 0 12px 28px rgba(0,0,0,0.45);
    overflow: hidden;
  }
  /* Contact side */
  .card--contact {
    background: linear-gradient(160deg, var(--card-black-top) 0%, #1c1c1c 45%, var(--card-black) 100%);
  }
  .card--contact .business-name {
    position: absolute;
    top: 94px;
    right: 40px;
    font-family: "Cinzel", serif;
    font-weight: 600;
    font-size: 21px;
    letter-spacing: 0.03em;
    text-transform: uppercase;
    color: var(--brand-yellow);
    white-space: nowrap;
  }
  .card--contact .divider {
    position: absolute;
    top: 140px;
    left: 200px;
    right: 40px;
    height: 1px;
    background: var(--rule-dark);
    box-shadow: 0 1px 0 rgba(255,255,255,0.08);
  }
  .card--contact .person-name {
    position: absolute;
    left: 38px;
    top: 178px;
    font-family: "Cinzel", serif;
    font-weight: 600;
    font-size: 18px;
    letter-spacing: 0.03em;
    text-transform: uppercase;
    color: var(--brand-yellow);
    white-space: nowrap;
  }
  .card--contact .phone {
    position: absolute;
    left: 50px;
    top: 210px;
    font-family: "Cormorant Garamond", serif;
    font-weight: 500;
    font-size: 22px;
    font-variant-numeric: lining-nums;
    color: var(--phone-grey);
    white-space: nowrap;
  }
  /* Brand side */
  .card--brand {
    background: var(--brand-yellow);
    display: flex;
    flex-direction: column;
    align-items: center;
    justify-content: center;
    gap: 14px;
  }
  .card--brand .business-name {
    font-family: "Cinzel", serif;
    font-weight: 600;
    font-size: 24px;
    letter-spacing: 0.03em;
    text-transform: uppercase;
    color: var(--ink-black);
    white-space: nowrap;
  }
  .card--brand .tagline {
    font-family: "Cinzel", serif;
    font-weight: 400;
    font-size: 12px;
    letter-spacing: 0.26em;
    text-transform: uppercase;
    color: var(--ink-black);
    white-space: nowrap;
  }
</style>
</head>
<body>
  <main class="stage">
    <section class="card card--contact">
      <p class="business-name">Treviske Roadside Repair</p>
      <div class="divider"></div>
      <p class="person-name">Marcello Treviske</p>
      <p class="phone">(555) 381-7094</p>
    </section>
    <section class="card card--brand">
      <p class="business-name">Treviske Roadside Repair</p>
      <p class="tagline">Fair prices at your door</p>
    </section>
  </main>
</body>
</html>
```